Forex website redesign

We need an attractive good looking website design that increase the apatite of our visitors to subscribe to our advisory service, beside the fact that we do offer very high quality service.

Our service is where we connect to investor accounts who are subscribed, to automatically deliver and execute our advise to buy or sell straight onto their account using high tech software.

The final design should communicate financial safty and growth.
Updates

Here is something to keep in mind about our business model that may help you in your design, we SHOW people the right way to invest, so they can make money instead of going somewere else and lose it. Beside that point, most websites in forex that includes pictures of happy and excited people who make money ALWAY turn out to be scam. So please try not to position our business that way in visitor first impression once he/she visit our site.

Thank you for your help :)

Target Market(s)

Financial Market, 20-70 years old

Industry/Entity Type

Financial

Requirements
Must have
• Call to action feature + Logo redesign. Please visit www.brelvantrade.net to get an idea of how we want it. Also include the personal photos of our advisors in your deign.

```html
<!DOCTYPE html>
<html lang="en">
<head>
<meta charset="utf-8">
<title>Halvera FX – Forex Signals</title>
<link rel="stylesheet" href="https://fonts.googleapis.com/css2?family=Open+Sans:wght@400;600;700&family=Roboto:wght@300;400;700&display=swap">
<style>
:root{
  --ink:#333;
  --muted:#444;
  --brand:#1d4fb0;
  --brand-dark:#0d2f80;
  --navy:#0a2370;
  --sky:#3e97e0;
  --orange:#f5901e;
  --card:#fbfcfd;
  --green:#7bd23a;
}
*{margin:0;padding:0;box-sizing:border-box}
html,body{width:800px;height:1200px;overflow:hidden}
body{position:relative;background:linear-gradient(#e9eef3,#eef2f6 60%,#e5eaf0);font-family:"Open Sans",sans-serif;color:var(--ink)}
.abs{position:absolute}
.site-header{left:0;top:0;width:800px;height:102px;background:linear-gradient(#f2f3f5,#d9dde2);border-top:3px solid #c9d8ea}
.logo{left:232px;top:25px;display:flex;align-items:center;gap:12px}
.logo-mark{width:56px;height:56px;border-radius:50%;background:var(--brand)}
.logo-name{font-family:"Open Sans",sans-serif;font-weight:700;font-size:34px;color:var(--brand);letter-spacing:1px;line-height:1}
.main-nav{left:0;top:102px;width:800px;height:32px;background:linear-gradient(#1d4aa8,#0b2a78);display:flex;justify-content:center;border-bottom:1px solid #08205e}
.main-nav a{color:#fff;text-decoration:none;font-size:11px;padding:0 12px;line-height:32px;border-right:1px solid #0a235f}
.main-nav a:last-child{border-right:0}
.hero{left:67px;top:135px;width:666px;height:231px;background:linear-gradient(135deg,#6dc3f5,#2a7fd8 40%,#1f62c4 70%,#3c8fe0);overflow:hidden;box-shadow:0 12px 14px -8px #555}
.hero-title{top:10px;width:100%;text-align:center;color:#fff;font-family:"Roboto",sans-serif;font-weight:700;font-size:20px}
.hero-achieve{top:52px;width:100%;text-align:center;color:#fff;font-family:"Roboto",sans-serif;font-weight:700;font-size:42px;letter-spacing:22px;text-shadow:0 3px 5px #234}
.hero-results{top:108px;width:100%;text-align:center;color:#111;font-family:"Roboto",sans-serif;font-weight:300;font-size:40px;letter-spacing:-1px}
.hero-cta{left:246px;top:166px;width:174px;height:28px;border-radius:6px;background:#1a4f9a;color:#fff;font-family:"Roboto",sans-serif;font-weight:700;font-size:10.5px;text-align:center;line-height:28px}
.hero-dots{left:305px;top:209px;display:flex;gap:8px}
.hero-dots i{width:11px;height:11px;border-radius:50%;background:#1a3a80}
.hero-figure{left:500px;top:70px;width:100px;height:161px;background:linear-gradient(#233,#0a0f1a);border-radius:36px 36px 0 0;opacity:.8}
.intro{left:92px;top:391px;width:616px;text-align:center;font-size:18px;line-height:24px;color:var(--muted)}
.intro b{color:#333}
.feature-icon{width:58px;height:58px;border-radius:50%;top:503px;display:flex;align-items:center;justify-content:center}
.card{top:565px;width:207px;height:210px;background:var(--card);border-radius:6px}
.card h2{text-align:center;font-size:17px;font-weight:600;color:#444;margin-top:14px}
.card p{font-size:7.4px;line-height:10.6px;color:#444}
.read-more{display:flex;align-items:center;justify-content:space-between;width:88px;height:18px;border:1px solid #bbb;border-radius:9px;background:#fff;font-size:8px;color:#111;padding:0 8px 0 9px}
.read-more span{color:#2a9a2a;font-size:8px}
.advisor-photo{float:left;width:51px;height:56px;background:linear-gradient(#b8a79a,#6f5d54);margin:0 10px 2px 0}
.order-badge{left:138px;top:46px;width:54px;height:54px;border-radius:50%;background:var(--orange);color:#fff;font-family:"Roboto",sans-serif;font-weight:300;font-size:14px;line-height:15px;text-align:center;padding-top:11px}
.section-title{font-size:17.5px;font-weight:600;color:#333;display:flex;align-items:center;gap:8px}
.testimonial{left:80px;top:842px;width:420px;height:78px;background:linear-gradient(#e7e9e4,#f8f9f7);border-radius:6px;padding:21px 18px;font-size:7.4px;line-height:10px;color:#444}
.testimonial::before{content:"";position:absolute;left:38px;top:-8px;border:8px solid transparent;border-top:0;border-bottom-color:#e7e9e4}
.testimonial strong{display:block;font-size:10.5px;font-weight:600;color:#222;line-height:15px;margin-top:4px}
.risk-text{left:544px;top:844px;width:190px;font-size:7.4px;line-height:10.6px;color:#444}
.tagline{left:91px;top:978px;font-size:16px;font-weight:600;color:var(--brand)}
.tagline b{color:#111}
.tagline em{font-style:normal;color:var(--orange);margin-left:14px}
.newsletter-label{left:547px;top:961px;font-size:8px;color:#111}
.newsletter-input{left:539px;top:979px;width:145px;height:20px;border:1px solid #c4c9cf;background:#fff;font-size:8px;color:#777;padding:5px 7px}
.newsletter-btn{left:695px;top:984px;font-size:8px;color:#111}
.site-footer{left:0;top:1017px;width:800px;height:148px;background:radial-gradient(circle at 640px 40px,#3c74e6,#1f55c6 30%,#1a4cbb 70%)}
.footer-col{top:16px}
.footer-col h3{color:#fff;font-size:14.5px;font-weight:600;margin-bottom:9px}
.footer-col a{display:block;color:#fff;text-decoration:none;font-size:8px;line-height:15.5px}
.footer-col a.live{color:var(--green);font-weight:600}
.social{display:flex;gap:6px;margin-top:3px}
.social i{width:17px;height:17px;border-radius:50%;background:var(--navy)}
.footer-logo{left:550px;top:18px;display:flex;align-items:center;gap:7px}
.footer-logo .logo-mark{width:26px;height:26px;background:var(--navy)}
.footer-logo .logo-name{font-size:17px;color:var(--navy)}
.footer-copy{left:581px;top:63px;font-size:8px;color:#fff}
.footer-band{left:0;top:1165px;width:800px;height:35px;background:var(--navy)}
</style>
</head>
<body>

<header class="site-header abs">
  <div class="logo abs"><span class="logo-mark"></span><span class="logo-name">HALVERA FX</span></div>
</header>

<nav class="main-nav abs">
  <a href="#">Home</a><a href="#">About Us</a><a href="#">Order</a><a href="#">Performance »</a><a href="#">Arlo Brennan Special</a><a href="#">Terms &amp; Conditions</a><a href="#">Why Us?</a><a href="#">Contact Us</a>
</nav>

<section class="hero abs" role="img" aria-label="Blue trading chart background with laptops and a businessman with raised arms">
  <div class="hero-figure abs"></div>
  <div class="hero-title abs">The one stop shop for the best forex signals</div>
  <div class="hero-achieve abs">ACHIEVE</div>
  <div class="hero-results abs">THE HIGHEST RESULTS</div>
  <div class="hero-cta abs">Click here to See Live Results</div>
  <div class="hero-dots abs"><i></i><i></i><i></i><i></i></div>
</section>

<p class="intro abs"><b>Halvera FX LTD</b> is the ONLY forex signal service on this planet that provides full info about the traders involved including REAL personal photos, REAL personal details and portfolios, as well as YEARS of verified and consistent live trading performance.</p>

<div class="feature-icon abs" style="left:155px;background:var(--brand)">
  <svg width="24" height="22" viewBox="0 0 24 22"><rect x="1" y="1" width="22" height="15" rx="1.5" fill="none" stroke="#fff" stroke-width="2"/><rect x="9" y="17" width="6" height="2" fill="#fff"/><rect x="6" y="19" width="12" height="2" fill="#fff"/></svg>
</div>
<div class="feature-icon abs" style="left:382px;background:var(--sky)">
  <svg width="24" height="24" viewBox="0 0 24 24"><circle cx="12" cy="12" r="7" fill="none" stroke="#fff" stroke-width="2" stroke-dasharray="3 2"/><circle cx="12" cy="12" r="3" fill="none" stroke="#fff" stroke-width="2"/></svg>
</div>
<div class="feature-icon abs" style="left:604px;background:#4a4a4a">
  <svg width="24" height="24" viewBox="0 0 24 24"><rect x="2" y="10" width="5" height="11" fill="#3e97e0"/><path d="M8 10 L13 3 Q15 3 15 6 L14 9 H20 Q22 10 21 12 L19 20 Q18 21 16 21 H8 Z" fill="#3e97e0"/></svg>
</div>

<article class="card abs" style="left:78px">
  <h2>About Us</h2>
  <div class="abs" style="left:14px;top:48px;width:185px">
    <div class="advisor-photo" role="img" aria-label="Portrait photo of the lead advisor"></div>
    <p style="padding-top:2px">We are a group of investors who are mainly interested in Forex. Our non-stop search for Forex elite traders has began back in 2003, we have read and analyzed countless number of portfolios and we have developed advance and superior analytic skills over time and have built up a wide connection with what we believe are the best Forex traders on this planet.</p>
  </div>
  <div class="read-more abs" style="left:13px;top:176px">Read More <span>····›</span></div>
</article>

<article class="card abs" style="left:307px">
  <h2>How Signals Work</h2>
  <p class="abs" style="left:11px;top:48px;width:188px">Once you subscribe, you will be re-directed to a secure page to download and set-up the EA copier on your VPS with all the instructions you need(We provide full support, and we can set it up for you for no additional charge.<br><br>Once set-up, the software is of superior quality and copies flawlessly, and you have direct and total control over your account. Whereas your subscription will be renewed automatically</p>
  <div class="read-more abs" style="left:10px;top:176px">Read More <span>····›</span></div>
</article>

<article class="card abs" style="left:534px">
  <h2>Order Now</h2>
  <p class="abs" style="left:11px;top:46px;width:130px;font-size:12.5px;line-height:17px;color:#333">Let us do the picks, while you enjoy the</p>
  <div class="order-badge abs">Order<br>Now</div>
  <p class="abs" style="left:11px;top:111px;width:190px">Once set-up, the software is of superior quality and copies flawlessly, and you have direct and total control over your account. Whereas your subscription will be renewed automatically by the end of the cycle you choose (Monthly/OR/4 ..</p>
  <div class="read-more abs" style="left:10px;top:176px">Read More <span>····›</span></div>
</article>

<h2 class="section-title abs" style="left:92px;top:800px">
  <svg width="28" height="22" viewBox="0 0 28 22"><ellipse cx="16" cy="9" rx="11" ry="7" fill="#1d4fb0"/><path d="M18 14 L22 20 L14 15 Z" fill="#1d4fb0"/><ellipse cx="9" cy="12" rx="8" ry="5" fill="#3e97e0"/><path d="M5 16 L2 21 L9 16 Z" fill="#3e97e0"/></svg>
  Testimonials
</h2>
<div class="testimonial abs">Loren text we have developed advance and superior analytic skills over time and have built up a wide connection with what we believe are the best Forex traders on this planet.<strong>Mira Castell<br>USA</strong></div>
<div class="read-more abs" style="left:91px;top:934px">Read More <span>····›</span></div>

<h2 class="section-title abs" style="left:543px;top:801px">
  <svg width="21" height="21" viewBox="0 0 21 21"><circle cx="10.5" cy="10.5" r="8.5" fill="none" stroke="#0d2f80" stroke-width="3"/><line x1="4.5" y1="4.5" x2="16.5" y2="16.5" stroke="#0d2f80" stroke-width="3"/></svg>
  Risk Disclaimer
</h2>
<p class="risk-text abs">Once set-up, the software is of superior quality and copies flawlessly, and you have direct and total control over your account. Whereas your subscription will be renewed automatically by the end of the cycle you choose (Monthly/OR/4 months).</p>
<div class="read-more abs" style="left:539px;top:928px">Read More <span>····›</span></div>

<div class="tagline abs">you enjoy the financial safty <b>and growth</b><em>Order Now</em></div>
<div class="newsletter-label abs">Newsletter</div>
<div class="newsletter-input abs">enter yur email address</div>
<div class="newsletter-btn abs">Subscirbe</div>

<footer class="site-footer abs">
  <div class="footer-col abs" style="left:92px"><h3>ABOUT US</h3><a href="#">COMPANY INFO</a><a href="#">SERVICES</a><a href="#">TEAM</a><a href="#">SOLUTIONS</a></div>
  <div class="footer-col abs" style="left:215px"><h3>ADVICE</h3><a href="#">FAQS</a><a href="#">ACCOUNT</a><a href="#">CONTACTS</a><a href="#" class="live">Live Chat</a></div>
  <div class="footer-col abs" style="left:323px"><h3>JOIN IN</h3><a href="#">SIGN UP</a><a href="#">FORUMS</a><a href="#">PROMOTIONS</a></div>
  <div class="footer-col abs" style="left:424px"><h3>FOLLOW US</h3><div class="social"><i></i><i></i><i></i><i></i></div></div>
  <div class="footer-logo abs"><span class="logo-mark"></span><span class="logo-name">HALVERA FX</span></div>
  <div class="footer-copy abs">© 2013 | PRIVACY POLICY</div>
</footer>
<div class="footer-band abs"></div>

</body>
</html>
```